New Business Card Design Project

We require a business card design for Zelvaquin, a newly established Indian company.
Our focus is on the development, manufacturing, and export of a diverse array of pharmaceutical products on a global scale. The card should convey a professional appearance, as our primary markets are in Africa, China, and Southeast Asian nations.
We envision a two-sided business card, with the reverse side dedicated to a logo set against a solid color or an elegantly designed pattern. The corners should be rounded. We would appreciate seeing both horizontal and vertical design options. We trust the designer to utilize their expertise in creating this design.

The content for the business card is included in the attached Word file.

Target Market(s)

Our primary markets are in Africa, China, and Southeast Asian, Latin America, Maldives, Sri Lanka

Industry/Entity Type

Pharmaceutical Manufacturing and Export

Contact Information for Business Card

Colors

Designer to choose colors to be used in the design.

Requirements
Must have
• The reverse side of the business card features solely the logo along with the tagline, "Health, Delivered."
Should not have
• The logo should not exceed two instances, encompassing both the front and back sides of the card.

```html
<!DOCTYPE html>
<html lang="en">
<head>
<meta charset="utf-8">
<title>Zelvaquin Business Card</title>
<link href="https://fonts.googleapis.com/css2?family=Montserrat:wght@400;500;700&display=swap" rel="stylesheet">
<style>
  :root {
    --backdrop: #737373;
    --brand-blue: #27a9e1;
    --brand-coral: #f0604d;
    --paper: #ffffff;
    --ink-grey: #555555;
  }
  * { margin: 0; padding: 0; box-sizing: border-box; }
  html, body { width: 1200px; height: 1000px; overflow: hidden; }
  body {
    background: var(--backdrop);
    font-family: "Montserrat", Arial, sans-serif;
    position: relative;
  }
  .card {
    position: absolute;
    left: 293px;
    width: 614px;
    height: 352px;
    border-radius: 30px;
    overflow: hidden;
  }
  .card--reverse { top: 115px; background: var(--brand-blue); color: var(--paper); }
  .card--front { top: 517px; background: var(--paper); }

  .reverse-brand { position: absolute; left: 365px; top: 240px; text-align: left; }
  .reverse-brand__name { font-weight: 700; font-size: 38px; line-height: 1; letter-spacing: 0.2px; }
  .reverse-brand__tagline { font-weight: 400; font-size: 21px; line-height: 1.2; margin-top: 4px; }

  .holder { position: absolute; left: 57px; top: 76px; }
  .holder__name { color: var(--brand-blue); font-weight: 700; font-size: 17px; }
  .holder__role { color: var(--brand-coral); font-weight: 400; font-size: 16px; margin-top: 2px; }

  .brand-mark {
    position: absolute; right: 46px; top: 122px;
    display: flex; align-items: center; gap: 8px;
    color: var(--brand-blue); font-weight: 700; font-size: 28px;
  }
  .brand-mark__dot { width: 12px; height: 12px; border-radius: 50%; background: var(--brand-coral); }

  .contacts { position: absolute; left: 55px; top: 218px; list-style: none; }
  .contacts__item {
    display: flex; align-items: flex-start; gap: 10px;
    color: var(--ink-grey); font-size: 13px; line-height: 16px; margin-bottom: 12px;
  }
  .contacts__icon { width: 14px; height: 16px; flex: none; }

  .website { position: absolute; right: 62px; top: 293px; font-size: 15px; color: var(--ink-grey); }
  .website__name { color: var(--brand-blue); font-weight: 700; }
</style>
</head>
<body>
  <section class="card card--reverse" aria-label="Card reverse">
    <div class="reverse-brand">
      <div class="reverse-brand__name">Zelvaquin</div>
      <div class="reverse-brand__tagline">Health, Delivered</div>
    </div>
  </section>

  <section class="card card--front" aria-label="Card front">
    <div class="holder">
      <div class="holder__name">Arjun K. Velankar</div>
      <div class="holder__role">CEO</div>
    </div>

    <div class="brand-mark">
      <span class="brand-mark__dot"></span>
      <span>Zelvaquin</span>
    </div>

    <ul class="contacts">
      <li class="contacts__item">
        <svg class="contacts__icon" viewBox="0 0 14 16" aria-hidden="true">
          <path d="M7 1a4.5 4.5 0 0 0-4.5 4.5C2.5 9 7 14 7 14s4.5-5 4.5-8.5A4.5 4.5 0 0 0 7 1z" fill="var(--brand-blue)"/>
          <circle cx="7" cy="5.5" r="1.6" fill="#fff"/>
        </svg>
        <span>14, Sarovar Colony, Amravati,<br>444601, India</span>
      </li>
      <li class="contacts__item">
        <svg class="contacts__icon" viewBox="0 0 14 16" aria-hidden="true">
          <rect x="0" y="4" width="14" height="9" fill="var(--brand-blue)"/>
          <path d="M0.5 4.5 7 9.5 13.5 4.5" fill="none" stroke="#fff" stroke-width="1.2"/>
        </svg>
        <span>avelankar@zelvaquin.com</span>
      </li>
      <li class="contacts__item">
        <svg class="contacts__icon" viewBox="0 0 14 16" aria-hidden="true">
          <rect x="2.5" y="0.8" width="9" height="14.4" rx="1.5" fill="none" stroke="var(--brand-blue)" stroke-width="1.6"/>
          <circle cx="7" cy="12.5" r="0.9" fill="var(--brand-blue)"/>
        </svg>
        <span>+919800012345</span>
      </li>
    </ul>

    <div class="website"><span class="website__name">zelvaquin</span>.com</div>
  </section>
</body>
</html>
```